Financial Markets Algorithmic Trading solution needs One pager Marketing designs

We are creating Marketing sheets that will be handed to potential clients that will give a broad base of our products available. We are an established Sell side firm in the financial Industry and our product focus is a Technology base solution and we want to showcases our Algorithmic trading suite.
Our customer base is Buy-side Traders,hedge funds, managing directors. We want a clean high end technology based look that will encompass the colors that are in our logo.
We intend to work with the designer after initial design to encompass the theme to other pages we have. So we will need a design that can be part of a set but can stand alone.

** i have uploaded a new File that is the correct File to design to. Please follow the flow of the categories and what resides under those headers. This is key for the delivery of the material****

Target Market(s)

Finance- Buy side firms, geared for meetings and info sheets to be left with clients who are CEO's , Head Traders, Managing Directors

Industry/Entity Type

Financial Service

Font styles to use
Other font styles liked:
• Tw Cen MT

Requirements
Must have
• Must include the logo, and encompass the colors that are in the logo.
• We want this to have a Technology company feel to it. We would like it clean and unique, all while not falling into the normal classic business look.
• Also for this page we would like to keep the layout similar to what we have.
• Please keep the style of lettering
Should not have
• Messy look, overpowering color. no cartoon graphics

```html
<!DOCTYPE html>
<html lang="en">
<head>
<meta charset="utf-8">
<title>Algorithmic Trading Strategy Overview</title>
<link rel="stylesheet" href="https://fonts.googleapis.com/css2?family=Jost:wght@300;400;600;700&display=swap">
<style>
:root{
  --page:#e4e5e8;
  --orange:#f39322;
  --blue:#0c7bc4;
  --navy:#13213b;
  --ink:#2b303b;
  --rule:#6b7080;
  --hero-a:#a9aec0;
  --hero-b:#c9d5e3;
  --sky-a:#d8ebf5;
  --sky-b:#8fc3e2;
  --paper:#eef1f6;
}
*{margin:0;padding:0;box-sizing:border-box}
html,body{width:960px;height:1200px;overflow:hidden;background:var(--page)}
body{font-family:"Jost",sans-serif;color:var(--ink)}
.sheet{position:absolute;left:84px;top:40px;width:792px;height:1120px;background:var(--paper);overflow:hidden}
.sheet svg.art{position:absolute;left:0;top:0}
.title{position:absolute;left:86px;top:52px;font-weight:700;font-size:21px;color:#fff;letter-spacing:.04em}
.title .lead{color:var(--orange)}
.intro-line{position:absolute;height:18px;font-weight:600;font-size:12.5px;line-height:18px;color:var(--navy);letter-spacing:.05em;text-align:justify;text-align-last:justify;white-space:nowrap}
.intro-line.ragged{text-align-last:left}
.intro-line .firm{font-size:16px;font-weight:700}
.brand{position:absolute;left:520px;top:226px;display:flex;align-items:center;gap:10px}
.brand-dot{width:40px;height:40px;border-radius:50%;background:var(--orange)}
.brand-name{font-weight:400;font-size:21px;color:var(--blue);letter-spacing:.01em}
.group-label{position:absolute;font-weight:600;font-size:14px;letter-spacing:.03em;white-space:nowrap;transform:translate(-50%,-50%) rotate(-90deg)}
.group-label.orange{color:var(--orange)}
.group-label.blue{color:var(--blue)}
.rule{position:absolute;background:var(--rule)}
.strategy{position:absolute;left:60px}
.strategy h3{font-weight:600;font-size:11px;letter-spacing:.08em;color:var(--ink);margin-bottom:3px}
.strategy p{font-weight:300;font-size:10px;line-height:14.5px;letter-spacing:.03em;color:var(--ink)}
</style>
</head>
<body>
<div class="sheet">
  <svg class="art" width="792" height="1120" viewBox="0 0 792 1120">
    <defs>
      <linearGradient id="hero" x1="0" y1="0" x2="1" y2="0">
        <stop offset="0" stop-color="var(--hero-a)"/>
        <stop offset="1" stop-color="var(--hero-b)"/>
      </linearGradient>
      <linearGradient id="sky" x1="0" y1="0" x2="0" y2="1">
        <stop offset="0" stop-color="var(--sky-b)"/>
        <stop offset="1" stop-color="var(--sky-a)"/>
      </linearGradient>
      <linearGradient id="flame" x1="0" y1="0" x2="0" y2="1">
        <stop offset="0.6" stop-color="var(--orange)"/>
        <stop offset="1" stop-color="var(--orange)" stop-opacity="0"/>
      </linearGradient>
      <radialGradient id="machine" cx="0.55" cy="0.55" r="0.55">
        <stop offset="0" stop-color="#1d2233"/>
        <stop offset="0.6" stop-color="#3a4258"/>
        <stop offset="1" stop-color="#3a4258" stop-opacity="0"/>
      </radialGradient>
    </defs>
    <rect x="0" y="0" width="792" height="408" fill="url(#hero)" role="img" aria-label="Soft technical backdrop of interlocking gears"/>
    <polygon points="430,165 792,165 792,1120 680,1120 430,870" fill="url(#sky)"/>
    <polygon points="625,535 792,370 792,410 650,545" fill="#fff" opacity=".8"/>
    <polygon points="451,245 526,165 792,165 792,325 526,325" fill="#fff" opacity=".95"/>
    <polygon points="78,23 124,66 78,108" fill="#fff"/>
    <polygon points="27,105 91,48 91,160" fill="var(--orange)"/>
    <polygon points="426,350 676,600 426,850" fill="url(#flame)"/>
    <polygon points="291,413 423,283 423,543" fill="var(--blue)"/>
    <rect x="360" y="690" width="432" height="430" fill="url(#machine)" role="img" aria-label="Illustration of large dark machined gears"/>
  </svg>

  <h1 class="title"><span class="lead">Alg</span>orithmic Trading Strategy Overview</h1>

  <div class="intro-line" style="left:98px;top:106px;width:448px"><span class="firm">Larkmont &amp; Partners</span> has partnered with an award winning</div>
  <div class="intro-line" style="left:98px;top:124px;width:428px">algorithmic trading platform and developed a custom suite of</div>
  <div class="intro-line" style="left:98px;top:142px;width:412px">algorithms designed to ensure high quality execution.&nbsp; Our</div>
  <div class="intro-line" style="left:44px;top:160px;width:446px">algorithms incorporate our unique Meridian point of sale order types</div>
  <div class="intro-line" style="left:44px;top:178px;width:427px">(aQuote* / bQuote*) seamlessly into each strategy. This</div>
  <div class="intro-line" style="left:44px;top:196px;width:408px">integration smooth's workflow, improves execution quality,</div>
  <div class="intro-line" style="left:44px;top:214px;width:390px">ensures greater liquidity sourcing, minimizes information</div>
  <div class="intro-line" style="left:44px;top:232px;width:371px">leakage and brings a wide variety of Algo and SOR</div>
  <div class="intro-line" style="left:44px;top:250px;width:352px">strategies directly into your OMS, EMS, or proprietary</div>
  <div class="intro-line" style="left:44px;top:268px;width:335px">trading platform. In addition, we work in a</div>
  <div class="intro-line ragged" style="left:44px;top:286px;width:316px">consultative role to develop custom DMA routes,</div>
  <div class="intro-line ragged" style="left:44px;top:304px;width:298px">design algorithms according to client needs or</div>
  <div class="intro-line ragged" style="left:44px;top:322px;width:280px">specific requirements, &amp; implement unique</div>
  <div class="intro-line ragged" style="left:44px;top:340px;width:262px">routing strategies designed to efficiently</div>
  <div class="intro-line" style="left:44px;top:358px;width:243px">touch today's complex market</div>
  <div class="intro-line ragged" style="left:44px;top:376px;width:200px">micro-strategy.</div>

  <div class="brand"><span class="brand-dot"></span><span class="brand-name">larkmont&amp;partners</span></div>

  <div class="rule" style="left:51px;top:423px;width:245px;height:1px"></div>
  <div class="rule" style="left:51px;top:423px;width:1px;height:182px"></div>
  <div class="group-label orange" style="left:40px;top:535px">Liquidity Sourcing</div>
  <div class="strategy" style="top:432px;width:310px">
    <h3>“SOR”</h3>
    <p>Optimizes order placement in lit and dark venues<br>to maximize liquidity capture and minimize information<br>leakage. The strategy balances “Urgency to capture the<br>display quote” vs. opportunities to seek out dark liquidity to<br>minimize information leakage and price improvement.</p>
  </div>
  <div class="strategy" style="top:535px;width:370px">
    <h3>DARK AGG</h3>
    <p>Manages order placement in dark venues to optimize liquidity capture<br>and reduce information leakage. The strategy attempts to first discover<br>liquidity by slicing optimally sized orders at various venues, and then<br>rebalances intelligently to venues where it has detected liquidity.</p>
  </div>

  <div class="rule" style="left:51px;top:655px;width:370px;height:1px"></div>
  <div class="rule" style="left:51px;top:655px;width:1px;height:156px"></div>
  <div class="group-label blue" style="left:40px;top:748px">Schedule Driven</div>
  <div class="strategy" style="top:666px;width:370px">
    <h3>“VWAP”</h3>
    <p>Trades using historical volume profile to target VWAP as the benchmark.<br>The strategy can optionally accept StartTime and EndTime as parameters<br>to schedule trading in a given trading period. The strategy utilizes<br>passive and aggressive trading tactics to achieve liquidity.</p>
  </div>
  <div class="strategy" style="top:754px;width:300px">
    <h3>“TWAP”</h3>
    <p>Similar to the VWAP strategy with a different schedule.<br>The schedule is a constant rate of trading between the<br>given StartTime and EndTime.</p>
  </div>

  <div class="rule" style="left:51px;top:865px;width:330px;height:1px"></div>
  <div class="rule" style="left:51px;top:865px;width:1px;height:156px"></div>
  <div class="group-label orange" style="left:40px;top:940px">Dynamic &amp; Adaptive</div>
  <div class="strategy" style="top:873px;width:330px">
    <h3>“POV”</h3>
    <p>Tracks volume from the time the order starts trading and trades<br>according to the specified target participation percentage.<br>Continuous optimizations are made as the order trades to<br>target optima price and liquidity goals.</p>
  </div>
  <div class="strategy" style="top:961px;width:230px">
    <h3>“ARRIVAL PRICE”</h3>
    <p>Manages the trade-off between market<br>impact and volatility (price risk) to<br>optimally execute the order.</p>
  </div>
</div>
</body>
</html>
```